Lomi Vardell
Incorporated
Lomi Vardell -
Creative Brief
Use specific fonts
Please use font that would fulfill the requirements of the comment description below
Professional
Derek Holm
Operations Manager
City of Brenmoor, CA
lomivardell@quillmesh.net
Our company extracts essential and fragrance oil from flowers. We blend our own brand-name perfume and fragrances. Please design cards to reflect a corporate appeal, with feminine luxury, higher end sophistication, yet gentle and soft. Attached is chosen logo. Feel free to take the abstract symbol and name out of the background if deemed necessary.

```html
<!DOCTYPE html>
<html lang="en">
<head>
<meta charset="utf-8">
<title>Lomi Vardell – Business Card</title>
<link rel="stylesheet" href="https://fonts.googleapis.com/css2?family=Source+Sans+3:wght@400;600;700&display=swap">
<style>
  :root {
    --backdrop: #8c4a1f;
    --card-grey: #8e8e8e;
    --gold-light: #f3dfa6;
    --gold-mid: #d9b770;
    --gold-deep: #b08a45;
    --ink: #1c1a18;
    --ink-soft: #2a2622;
    --mark-brown: #5a3a22;
  }
  * { margin: 0; padding: 0; box-sizing: border-box; }
  html, body {
    width: 1200px; height: 529px; overflow: hidden;
    background: var(--backdrop);
    font-family: "Source Sans 3", "Myriad Pro", Arial, sans-serif;
    color: var(--ink);
  }
  .stage { position: relative; width: 1200px; height: 529px; }

  .card {
    position: absolute; top: 106px;
    width: 528px; height: 316px;
    border-radius: 18px; overflow: hidden;
    background: var(--card-grey);
  }
  .card--front { left: 62px; }
  .card--back { left: 626px; }

  .gold-band {
    position: absolute; left: 0; right: 0;
    background: linear-gradient(90deg, var(--gold-deep) 0%, var(--gold-light) 45%, var(--gold-mid) 75%, var(--gold-deep) 100%);
  }
  .gold-band--top { top: 0; height: 74px; }
  .gold-band--bottom { bottom: 0; height: 50px; }

  .holder { position: absolute; right: 24px; top: 16px; }
  .holder__name { font-size: 27px; font-weight: 700; line-height: 1; color: var(--ink); }
  .holder__title { font-size: 12px; margin-top: 6px; color: var(--ink-soft); }

  .brand__dot {
    position: absolute; left: 77px; top: 80px;
    width: 52px; height: 52px; border-radius: 50%;
    background: var(--mark-brown);
  }
  .brand__name {
    position: absolute; left: 6px; top: 136px;
    font-size: 21px; letter-spacing: 4px; line-height: 24px;
    text-transform: uppercase; color: var(--ink);
  }

  .contact {
    position: absolute; left: 0; right: 0; top: 212px;
    text-align: center; font-size: 16px; line-height: 23px; color: var(--ink);
  }

  .back-mark__dot {
    position: absolute; left: 199px; top: 74px;
    width: 130px; height: 130px; border-radius: 50%;
    background: var(--mark-brown);
  }
  .back-mark__name {
    position: absolute; left: 0; right: 0; top: 212px;
    text-align: center; font-size: 16px; letter-spacing: 3px; line-height: 20px;
    text-transform: uppercase; color: var(--ink);
  }
  .back-email {
    position: absolute; left: 0; right: 0; top: 252px;
    text-align: center; font-size: 14px; font-weight: 700; line-height: 18px; color: var(--ink);
  }
</style>
</head>
<body>
<main class="stage">
  <section class="card card--front" aria-label="Business card front">
    <div class="gold-band gold-band--top"></div>
    <div class="holder">
      <p class="holder__name">Derek Holm</p>
      <p class="holder__title">Operations Manager</p>
    </div>
    <span class="brand__dot" aria-hidden="true"></span>
    <p class="brand__name">Lomi Vardell</p>
    <div class="contact">
      <p>City of Brenmoor, CA Pone: (555)468-0142</p>
      <p>Email: lomivardell@quillmesh.net</p>
    </div>
    <div class="gold-band gold-band--bottom"></div>
  </section>

  <section class="card card--back" aria-label="Business card back">
    <span class="back-mark__dot" aria-hidden="true"></span>
    <p class="back-mark__name">Lomi Vardell</p>
    <p class="back-email">Email: lomivardell@quillmesh.net</p>
  </section>
</main>
</body>
</html>
```